Brett Olsen Building Business Card Design

Hi,

I need a business card for my Building company.
I am a Builder and build homes for clients.
I am looking for a sophisticated logo that can be used on business cards, envelopes and letter heads.
I am trying to take my business to the next level and need a professional business card.

Colours: Please use white, black, dark grey and bright blue.

Thank you,

Carol and Brett.

Target Market(s)

1. Home and Building Companies 2. Potential customers

Industry/Entity Type

Business

Contact Information for Business Card

Brett Olsen Building PTY LTD

Brett Olsen

Director

A.B.N. 37 829 516 073

BUILDERS LICENCE No. 573019k

Mobile: 0412 907 381

Email: brettolsenbuilding@mailvane.com.au

Requirements
Must have
• The following is compulsory to have in the designs:

Brett Olsen Building PTY LTD (business name)

Brett Olsen (contact name)

Director (position)

A.B.N. 37 829 516 073

Builders Licence No. 573019k

Mobile: 0412 907 381

Nice to have
• Logo for business
Should not have
• Should not be cluttered.

I am looking for a clean, sophisticated and professional business card design.

```html
<!DOCTYPE html>
<html lang="en">
<head>
<meta charset="utf-8">
<title>Brett Olsen Building – Business Card</title>
<link href="https://fonts.googleapis.com/css2?family=Russo+One&family=Questrial&display=swap" rel="stylesheet">
<style>
  :root {
    --page: #ffffff;
    --card-light: #f4f4f4;
    --card-edge: #cfcfcf;
    --brand-blue: #29abe2;
    --deep-blue: #1687b8;
    --rule-grey: #a3a3a3;
    --mark-grey: #9e9e9e;
    --text-grey: #555555;
    --ink: #111111;
    --white: #ffffff;
  }
  * { margin: 0; padding: 0; box-sizing: border-box; }
  html, body {
    width: 1200px; height: 900px; overflow: hidden;
    background: var(--page);
  }
  .sheet { position: relative; width: 1200px; height: 900px; }

  .card {
    position: absolute; left: 267px; width: 666px;
    border: 1px solid var(--card-edge);
  }
  .card--front {
    top: 33px; height: 411px;
    background: radial-gradient(ellipse at 50% 45%, #ffffff 0%, var(--card-light) 60%, #ececec 100%);
  }
  .card--back {
    top: 457px; height: 410px;
    background: var(--brand-blue);
  }

  .brand-mark {
    position: absolute; left: 0; right: 0; top: 128px;
    display: flex; align-items: center; justify-content: center; gap: 16px;
  }
  .brand-mark__square {
    width: 34px; height: 34px; background: var(--brand-blue);
  }
  .brand-mark__name {
    font-family: "Questrial", sans-serif; font-size: 30px;
    color: var(--mark-grey); letter-spacing: 1px;
  }

  .company-name {
    position: absolute; left: 34px; right: 34px; top: 254px;
    text-align: center; white-space: nowrap;
    font-family: "Russo One", sans-serif; font-size: 33px;
    color: var(--brand-blue); letter-spacing: 1px;
  }
  .company-name__suffix { font-size: 16px; margin-left: 6px; }

  .rule {
    position: absolute; left: 34px; width: 600px; height: 5px;
  }
  .rule--grey { top: 309px; background: var(--rule-grey); }
  .rule--blue {
    top: 279px; left: 28px; height: 5px;
    background: var(--deep-blue);
    box-shadow: 0 1px 2px rgba(0,0,0,0.25);
  }

  .registration {
    position: absolute; left: 0; right: 0; top: 329px;
    text-align: center; font-family: "Questrial", sans-serif;
    font-size: 13px; line-height: 20px; color: var(--text-grey);
  }

  .contact-name {
    position: absolute; left: 0; right: 0; top: 46px;
    text-align: center; font-family: "Russo One", sans-serif;
    font-size: 46px; color: var(--white); letter-spacing: 2px;
  }
  .house-sketch {
    position: absolute; left: 211px; top: 105px; width: 242px; height: 155px;
    background: radial-gradient(ellipse at 55% 55%, rgba(255,255,255,0.35) 0%, rgba(255,255,255,0.08) 70%, rgba(255,255,255,0) 100%);
  }
  .position-title {
    position: absolute; left: 0; right: 0; top: 292px;
    text-align: center; font-family: "Questrial", sans-serif;
    font-size: 26px; color: var(--white);
  }
  .contact-lines {
    position: absolute; left: 0; right: 0; top: 330px;
    text-align: center; font-family: "Questrial", sans-serif;
    font-size: 13px; line-height: 19px; color: var(--ink);
  }
</style>
</head>
<body>
<main class="sheet">
  <section class="card card--front">
    <div class="brand-mark">
      <span class="brand-mark__square"></span>
      <span class="brand-mark__name">Brett Olsen Building</span>
    </div>
    <h1 class="company-name">BRETT OLSEN BUILDING<span class="company-name__suffix">PTY LTD</span></h1>
    <div class="rule rule--grey"></div>
    <p class="registration">A.B.N. 37 829 516 073<br>BUILDERS LICENCE No. 573019k</p>
  </section>

  <section class="card card--back">
    <h2 class="contact-name">BRETT OLSEN</h2>
    <div class="house-sketch" role="img" aria-label="Wireframe architectural sketch of a modern two-storey house"></div>
    <div class="rule rule--blue"></div>
    <p class="position-title">Director</p>
    <p class="contact-lines">Mobile: 0412 907 381<br>Email: brettolsenbuilding@mailvane.com.au</p>
  </section>
</main>
</body>
</html>
```